Start-up company developing economical and ecological hydrogen peroxide generator needs an attractiv

We need a powerpoint design for a start-up company based in Montreal called Vorbelle currently seeking to raise funds from investors. We develop an electrochemical hydrogen peroxide generator based on new generation catalysts.

These generators allow industrial users of hydrogen peroxide to generate it onsite economically and ecologically, as opposed to buying it from the major suppliers who make it large production plants using more polluting methods and need to transport it to customers over long distances.

We would like to see designs that have a cleantech technology and green chemistry feel. Colors that evoke a sense of environmental sustainability are desired.

The final design should communicate technological innovation that makes the world a cleaner and healthier place to live.

Target Market(s)

Industrial users or producers of of hydrogen peroxide

Industry/Entity Type

It Company

Font styles to use
Sans Serif

Colors
0255a3
3276b5
85acd3
9bcb3b
add136
e3eebf

Requirements
Must have
• Clean, attractive, professional and advanced technology look.
• Our slogan is: Catalyst for innovation
Nice to have
• The cover page should have our logo and our slogan. It should also have some graphics that pertain to technology and green chemistry. The perception that one should have when looking at it is that the company is developing a clean chemical manufacturing technology that is more environmentally friendly.
• Each other template page should have our logo discretely included in it.
• Other than the cover page, the template pages should not be too crowded with design elements. There should be lots of clear space to add material.
• I have uploaded some inspirational images that can be used to help come up with some designs.

```html
<!DOCTYPE html>
<html lang="en">
<head>
<meta charset="utf-8">
<title>Vorbelle – Slide Template</title>
<link href="https://fonts.googleapis.com/css2?family=Open+Sans:wght@400;600;700&display=swap" rel="stylesheet">
<style>
  :root{
    --page:#eef0f3;
    --slide:#ffffff;
    --blue:#0255a3;
    --blue-mid:#3276b5;
    --blue-light:#85acd3;
    --green:#9bcb3b;
    --ink:#1d1d1d;
    --muted:#666a70;
    --bar:#4a4d52;
    --photo-a:#8f9aa6;
    --photo-b:#c9cfd6;
  }
  *{box-sizing:border-box;margin:0;padding:0}
  html,body{width:849px;height:1200px;overflow:hidden}
  body{background:var(--page);font-family:"Open Sans",Arial,sans-serif;color:var(--ink);position:relative}

  .slide{position:absolute;left:57px;width:735px;height:560px;background:var(--slide);
    box-shadow:0 1px 4px rgba(0,0,0,.18);overflow:hidden}
  .slide--about{top:24px}
  .slide--services{top:630px}

  .slide__title{position:absolute;left:26px;top:14px;font-size:32px;font-weight:400;color:var(--blue);line-height:1.1}
  .slide__tagline{position:absolute;left:28px;top:54px;font-size:13px;color:var(--muted)}
  .slide__rule{position:absolute;left:12px;top:12px;width:4px;height:58px;background:var(--blue)}

  .brand{position:absolute;right:30px;top:22px;display:flex;align-items:center;gap:7px}
  .brand__dot{width:12px;height:12px;border-radius:50%;background:var(--green)}
  .brand__name{font-size:20px;font-weight:600;color:var(--blue)}

  .footer{position:absolute;left:0;right:0;bottom:0;height:26px;background:var(--bar)}
  .footer__num{position:absolute;right:0;top:0;width:150px;height:26px;background:var(--blue);
    color:#fff;font-size:13px;font-weight:600;display:flex;align-items:center;justify-content:flex-end;padding-right:40px}
  .footer__accent{position:absolute;left:0;top:-5px;width:100%;height:5px;background:var(--blue-light)}

  /* About */
  .about-band{position:absolute;left:0;right:0;top:146px;height:186px;background:var(--blue)}
  .about-band__text{position:absolute;left:0;top:0;width:252px;height:100%;padding:34px 22px 0 38px;
    color:#fff;font-size:16px;font-weight:600;line-height:1.35}
  .about-band__photo{position:absolute;left:252px;right:0;top:-16px;height:202px;
    background:linear-gradient(180deg,var(--photo-b) 0%,var(--photo-a) 55%,#2e3338 100%)}
  .about-body{position:absolute;left:256px;top:360px;width:440px;font-size:14px;line-height:1.45;color:var(--ink)}

  /* Services */
  .tiles{position:absolute;left:24px;top:92px;width:218px;display:grid;
    grid-template-columns:1fr 1fr;grid-auto-rows:84px;gap:3px}
  .tile--photo{background:linear-gradient(135deg,var(--photo-b),var(--photo-a))}
  .tile--text{background:var(--blue);color:#fff;font-size:11px;display:flex;align-items:center;justify-content:center}
  .columns{position:absolute;left:300px;top:92px;display:flex;gap:34px}
  .points{width:176px;list-style:none}
  .points li{position:relative;padding-left:12px;font-size:12px;line-height:1.35;color:#333;margin-bottom:12px}
  .points li::before{content:"";position:absolute;left:0;top:7px;width:4px;height:4px;border-radius:50%;background:var(--ink)}
</style>
</head>
<body>

<section class="slide slide--about">
  <div class="slide__rule"></div>
  <h1 class="slide__title">About us</h1>
  <p class="slide__tagline">Catalyst for innovation</p>
  <div class="brand"><span class="brand__dot"></span><span class="brand__name">Vorbelle</span></div>

  <div class="about-band">
    <p class="about-band__text">Financial Reporting to Investors, Creditors, and Boards Cash Management/Monitoring, including</p>
    <div class="about-band__photo" role="img" aria-label="Photo of a business team in suits"></div>
  </div>

  <p class="about-body">Financial Reporting to Investors, Creditors, and Boards Cash budgeting, analysis, forecasting, and KPIs US Commodity Tax Compliance Cleanup of historical books, and management of bookkeeping Process</p>

  <div class="footer"><div class="footer__accent"></div><div class="footer__num">01</div></div>
</section>

<section class="slide slide--services">
  <div class="slide__rule"></div>
  <h1 class="slide__title">What we do</h1>
  <p class="slide__tagline">Catalyst for innovation</p>
  <div class="brand"><span class="brand__dot"></span><span class="brand__name">Vorbelle</span></div>

  <div class="tiles">
    <div class="tile--photo" role="img" aria-label="Photo of hands holding a globe"></div>
    <div class="tile--text">Insert your text</div>
    <div class="tile--text">Insert your text</div>
    <div class="tile--photo" role="img" aria-label="Photo of colleagues at a laptop"></div>
    <div class="tile--photo" role="img" aria-label="Photo of a team meeting"></div>
    <div class="tile--text">Insert your text</div>
  </div>

  <div class="columns">
    <ul class="points">
      <li>Good design principles and practices enhance our agility from the start.</li>
      <li>Early and continuous delivery of working software that the customer values.</li>
      <li>Customer collaboration throughout the duration of the project.</li>
      <li>Building projects around motivated individuals.</li>
    </ul>
    <ul class="points">
      <li>Good design principles and practices enhance our agility from the start.</li>
      <li>Early and continuous delivery of working software that the customer values.</li>
      <li>Customer collaboration throughout the duration of the project.</li>
      <li>Building projects around motivated individuals.</li>
    </ul>
  </div>

  <div class="footer"><div class="footer__accent"></div><div class="footer__num">02</div></div>
</section>

</body>
</html>
```